Foldable creative restaurant menu

We require foldable restaurant menu to be placed on the each table, want it to look creative and modern with pages representing pictures of the dish not all dishes but few to represent what we do.Please get creative make sure its different, the colour should represent classy restaurant, not cheap and fast. The shape of the menu can be difference creative words must be easy to read and the logo must be in the menu here and there briefly.

Target Market(s)

Restaurant customers

Industry/Entity Type

Health And Wellness

Colors

Designer to choose colors to be used in the design.

Requirements
Must have
• foldable, must have good dish presentation pictures and must look modern and classy
Nice to have
• funky design and creative can be not just square foldable but can be interesting shape of menu.
Should not have
• boring plain spaces
• small writing
• dark pictures

```html
<!DOCTYPE html>
<html lang="en">
<head>
<meta charset="utf-8">
<title>Verdella Bistro Menu</title>
<link rel="stylesheet" href="https://fonts.googleapis.com/css2?family=Josefin+Sans:wght@300;400&family=Didact+Gothic&display=swap">
<style>
:root{
  --green:#4aa843;
  --white:#ffffff;
  --ink:#2a2a2a;
  --soft:#555555;
  --line:#cfcfcf;
}
*{margin:0;padding:0;box-sizing:border-box}
html,body{width:854px;height:1200px;overflow:hidden;background:var(--white)}
body{position:relative;font-family:"Didact Gothic",sans-serif;color:var(--ink)}
.panel{position:absolute;overflow:hidden}
.arch{border-radius:142px 142px 0 0}
.panel--green{background:var(--green);color:var(--white)}
.panel--outline{border:1px solid var(--line);border-bottom:none}
.deco{position:absolute;inset:0;pointer-events:none}
.heading{position:absolute;left:0;right:0;text-align:center;font-family:"Josefin Sans",sans-serif;font-weight:300;letter-spacing:1.5px;font-size:25px;line-height:1;color:var(--green);white-space:nowrap}
.panel--green .heading{color:var(--white)}
.content{position:absolute}
.item{margin-bottom:9px}
.name{font-size:7.8px;text-transform:uppercase;letter-spacing:.2px;line-height:1.25}
.name .price{margin-left:8px}
.desc{font-size:6.6px;line-height:1.32;color:var(--soft)}
.desc .opt{display:block;margin-top:4px;padding-left:8px;text-indent:-8px}
.panel--green .desc{color:#eef7ec}
.photo{position:absolute;box-shadow:0 2px 6px rgba(0,0,0,.25)}
.bev .sub{font-size:6.8px;text-transform:uppercase;margin-top:4px;line-height:1.25}
.bev .desc{font-size:6.4px;line-height:1.32}
.bev .gap{display:block;margin-top:3px}
.brand{position:absolute;left:0;right:0;text-align:center;font-family:"Josefin Sans",sans-serif;font-weight:300;color:var(--white)}
.note{position:absolute;left:0;right:0;text-align:center;font-family:"Didact Gothic",sans-serif;color:var(--white)}
</style>
</head>
<body>

<!-- Breakfast -->
<section class="panel panel--green arch" style="left:0;top:0;width:284px;height:598px">
  <div class="photo" role="img" aria-label="Photo of a toasted seeded sandwich with egg, ham and cheese on a white plate" style="left:44px;top:48px;width:196px;height:134px;background:linear-gradient(135deg,#f4f1ea,#d9b57a 45%,#f0e6d2)"></div>
  <svg class="deco" width="284" height="598"><circle cx="262" cy="137" r="8" fill="none" stroke="#fff" stroke-width="1"/></svg>
  <h2 class="heading" style="top:193px">BREAKFAST</h2>
  <div class="content" style="left:27px;top:223px;width:222px">
    <div class="item"><div class="name">Big Verdella Breakfast<span class="price">19</span></div><div class="desc">Choose from sourdough OR Turkish served with eggs, bacon, chipolata's, hash brown, spinach, tomato &amp; mushroom</div></div>
    <div class="item"><div class="name">Acai Bowl<span class="price">13</span></div><div class="desc">Choice of:<span class="opt" style="margin-top:0">(1) Zesty Detox – Acai pure, Frozen Raspberries, Banana, Apple Juice with garnish on</span><span class="opt">(2) Antioxidant – Acai pure, Frozen Berries, Avocado, coconut water with garnish on to</span><span class="opt">(3) Tropical Fest – Acai pure OR energy, Frozen Mango, Coconut Water with garnish on top</span><span class="opt">(4) Cocolicious – Verdant Palm Coconut, Banana, Coconut Water with garnish on top</span></div></div>
    <div class="item"><div class="name">Avocado Smash – V GF<span class="price">13</span></div><div class="desc">Feta, spinach &amp; avocado served on the sourdough</div></div>
    <div class="item"><div class="name">Bruschetta<span class="price">12</span></div><div class="desc">Toast served with a mix of tangy tomatoes, basil, red onion and garlic &amp; with Feta cheese and Balsamic Italian dressing as garnish.</div></div>
    <div class="item"><div class="name">Eggs Benedict<span class="price">10</span></div><div class="desc">Poached eggs, English muffin, sautéed baby spinach served with hollandaise</div></div>
    <div class="item"><div class="name">7-Seed Breakfast<span class="price">10</span></div><div class="desc">Deliciously toasted seven-seed Low Gluten bread topped with pesto sauce, served with ham, scrambled egg, four-leaf salad, sundried &amp; cherry tomatoes and feta cheese</div></div>
    <div class="item"><div class="name">Egg &amp; Bacon Roll<span class="price">10</span></div></div>
    <div class="item"><div class="name">Add On's</div><div class="desc">Spinach 2, Mushroom 2, Egg 2, Cheese 2, Avocado 3, Bacon 3, Ham 3, Chipolata's 3, Smoked salmon 5</div></div>
  </div>
</section>

<!-- Mains -->
<section class="panel panel--outline arch" style="left:286px;top:0;width:282px;height:598px">
  <svg class="deco" width="282" height="598"><circle cx="204" cy="166" r="8" fill="none" stroke="#bbb"/></svg>
  <h2 class="heading" style="top:42px">MAINS</h2>
  <div class="content" style="left:28px;top:72px;width:238px">
    <div class="item"><div class="name">Salmon Skin On<span class="price">25</span></div><div class="desc">Salmon fillet on the skin, grilled – THE WAY YOU LIKE IT.<br>Served with choices of the following:<br>garden salad – steamed vegetables – rice<br>ADD Sauce – hollandaise, lemon butter</div></div>
    <div class="item"><div class="name">Flavoured Rib Eye Steak<span class="price">25</span></div><div class="desc">Ribeye Steak (rare, medium or well done)<br>Served with TWO choices of the following:<br>Chips – Garden salad – steamed vegetables<br>ADD Sauce – Pepper, Mushroom OR Garlic</div></div>
    <div class="item"><div class="name">Lamb Shank<span class="price">25</span></div><div class="desc">Slow cooked lamb shank served with mashed potato &amp; vegetables (zucchini, carrot, broccoli) in tomato red wine mixed herb sauce</div></div>
    <div class="item"><div class="name">Roast of the Day (beef or pork)<span class="price">25</span></div><div class="desc">Roasted pork or beef served with mashed potato and vegetables (zucchini, carrot, broccoli) with gravy sauce (cooked with onion, celery, carrot, herb mix and red wine)</div></div>
    <div class="item"><div class="name">Pork Scallopini<span class="price">23</span></div><div class="desc">Medallions of pork fried in a mushroom white wine sauce with a steamed vegetables and mashed potato</div></div>
    <div class="item"><div class="name">Barramundi Fillet<span class="price">23</span></div><div class="desc">Barramundi fillet served on the bed of rice with creamy white wine sauce<br>Served with TWO choices of the following:<br>Chips – Garden salad – steamed vegetables<br>ADD Sauce – tartare, lemon butter</div></div>
    <div class="item"><div class="name">Italian Style Breastfillet with pesto sauce<span class="price">23</span></div><div class="desc">Grilled chicken breast fillet with steamed vegetables and pesto cream sauce</div></div>
    <div class="item"><div class="name">Club Sandwich<span class="price">20</span></div><div class="desc">Big 3 layers sandwich with chicken, bacon, eggs, tomato and lettuce, served with chips</div></div>
  </div>
  <div class="photo" role="img" aria-label="Photo of a chicken parmigiana with chips and a garden salad on a white plate" style="left:32px;top:426px;width:216px;height:144px;background:linear-gradient(120deg,#f7f4ec,#e7b35a 35%,#c9862f 55%,#6a9b3d 80%,#f2efe8)"></div>
</section>

<!-- Mains continued, sides, kids -->
<section class="panel panel--outline arch" style="left:570px;top:0;width:284px;height:598px">
  <svg class="deco" width="284" height="598"><circle cx="245" cy="390" r="70" fill="none" stroke="#e6e6e6"/><circle cx="245" cy="390" r="8" fill="none" stroke="#bbb"/></svg>
  <div class="content" style="left:29px;top:72px;width:232px">
    <div class="item"><div class="name">Mushroom Risotto<span class="price">20</span></div><div class="desc">Vegetarian mushroom risotto with Arborio rice</div></div>
    <div class="item"><div class="name">Chicken Parmigiana<span class="price">17</span></div><div class="desc">Lightly crumbed oven baked chicken breast topped with Napoli sauce, ham and mozzarella served with chips and garden salad</div></div>
    <div class="item"><div class="name">Chicken Carbonara Parmigiana<span class="price">17</span></div><div class="desc">Lightly crumbed oven baked chicken breast topped with bacon, garlic, cream sauce and mozzarella served with chip and garden salad</div></div>
    <div class="item"><div class="name">Nachos<span class="price">16</span></div><div class="desc">Corn chips, beef, salsa, tasty cheese, grilled to perfection</div></div>
    <div class="item"><div class="name">Salt and Pepper Squid<span class="price">15</span></div><div class="desc">Squid, wedges with light sour cream and sweet chilli sauce</div></div>
    <div class="item"><div class="name">Beef Burger<span class="price">15</span></div><div class="desc">Beef patty served with cheese, bacon, lettuce and tomato with Chips on the side<br>Choice of sauce – Tomato, BBQ or Tomato Relish</div></div>
    <div class="item"><div class="name">Fish and Chips<span class="price">12</span></div><div class="desc">Fish, chips, salad and tartar sauce</div></div>
    <div class="item"><div class="name">Soup of the Day<span class="price">8</span></div></div>
  </div>
  <h2 class="heading" style="left:0;top:332px">SIDES</h2>
  <div class="content" style="left:29px;top:362px;width:200px">
    <div class="item" style="margin-bottom:7px"><div class="name">Chips<span class="price">4</span></div></div>
    <div class="item" style="margin-bottom:7px"><div class="name">Garden Salad<span class="price">6</span></div></div>
    <div class="item"><div class="name">Rice<span class="price">3</span></div></div>
  </div>
  <h2 class="heading" style="top:428px">KID'S MEALS</h2>
  <div class="content" style="left:29px;top:458px;width:232px">
    <div class="item" style="margin-bottom:7px"><div class="name">Cardinale Pizza &amp; Chips<span class="price">10</span></div><div class="desc">Mozzarella cheese and Ham served with chips</div></div>
    <div class="item" style="margin-bottom:7px"><div class="name">Spaghetti Bolognese<span class="price">7</span></div></div>
    <div class="item" style="margin-bottom:7px"><div class="name">Spaghetti with Meatballs<span class="price">7</span></div></div>
    <div class="item" style="margin-bottom:7px"><div class="name">Cheeseburger and Chips<span class="price">7</span></div></div>
    <div class="item" style="margin-bottom:7px"><div class="name">Fish and Chips<span class="price">7</span></div></div>
    <div class="item" style="margin-bottom:7px"><div class="name">Chips and Nuggets<span class="price">7</span></div></div>
  </div>
</section>

<!-- Salad, pasta, hot beverage -->
<section class="panel panel--outline arch" style="left:0;top:606px;width:284px;height:594px">
  <svg class="deco" width="284" height="594"><circle cx="40" cy="252" r="8" fill="none" stroke="#bbb"/></svg>
  <h2 class="heading" style="top:86px">SALAD</h2>
  <div class="content" style="left:30px;top:114px;width:220px">
    <div class="item"><div class="name">Asian Chicken Fusion Salad<span class="price">15</span></div><div class="desc">Grilled chicken served with a medley of fresh salad greens, sesame nut crumb and a light sweet chilli, sesame and soy dressing</div></div>
    <div class="item"><div class="name">Caesar Salad<span class="price">15</span></div><div class="desc">Baby Cos lettuce, crispy bacon, garlic croutons, flaked parmesan cheese, boiled egg in Caesar dressing<br>ADD CHICKEN 4, SMOKED SALMON 5</div></div>
    <div class="item"><div class="name">House Salad<span class="price">10</span></div><div class="desc">Crispy lettuce mix, tomato, cucumber, spinach, red onion, Kalamata olives and feta cheese drizzled with house dressing<br>ADD CHICKEN 4, SMOKED SALMON 5</div></div>
  </div>
  <h2 class="heading" style="top:250px">PASTA</h2>
  <div class="content" style="left:30px;top:278px;width:220px">
    <div class="item"><div class="name">Fettuccine Carbonara<span class="price">15</span></div><div class="desc">Fettuccine served with pan seared sliced ham, bacon, shallots and onion in a creamy garlic sauce</div></div>
    <div class="item"><div class="name">Fettuccine Matriciana <svg width="8" height="8" style="vertical-align:-1px"><circle cx="4" cy="4" r="4" fill="var(--green)"/></svg><span class="price">15</span></div><div class="desc">Fettuccine served with sun dried tomatoes, capsicum, zucchini, mushroom, onion, shallot and garlic in a Napoli sauce</div></div>
    <div class="item"><div class="name">Spaghetti Bolognese<span class="price">15</span></div><div class="desc">Spaghetti cooked al dente and pan tossed with a traditional Italian style meat sauce</div></div>
  </div>
  <h2 class="heading" style="top:386px">HOT BEVERAGE</h2>
  <div class="content" style="left:30px;top:418px;width:220px">
    <div class="item"><div class="name">Coffees</div><div class="desc">Espresso, Americano, Flat White, Latte, Piccolo Latte, Chai Latte, Chai Tea, Cappuccino, Macchiato, Babyccino<br>Cup 3.5 Mug 4.5 Takeaway 4.9 (small 3.9)</div></div>
    <div class="item"><div class="desc">HOT CHOCOLATE Cup 3.8 Mug 4.8 Takeaway 5.2<span class="opt" style="padding-left:0;text-indent:0">MOCHACCHINO Cup 2.5 Mug 3.5 Takeaway 4</span><span class="opt" style="padding-left:0;text-indent:0">HOT TEA 4.5 English Breakfast, Earl Grey, Sencha, Chamomile, Mint, Lemongrass, Chai</span></div></div>
    <div class="item"><div class="desc">Please select your choice of coffee design<br>Decafe 0.6, Vanilla 0.8, Hazelnut 0.8, Caramel 0.8, Chai 0.8</div></div>
  </div>
</section>

<!-- Chilled beverage -->
<section class="panel panel--green arch" style="left:286px;top:606px;width:282px;height:594px">
  <svg class="deco" width="282" height="594"><circle cx="282" cy="490" r="160" fill="none" stroke="#fff" stroke-opacity=".55"/></svg>
  <h2 class="heading" style="top:86px;font-size:23px;letter-spacing:.8px">CHILLED BEVERAGE</h2>
  <div class="content bev" style="left:30px;top:113px;width:236px">
    <div class="sub">Iced Drinks</div><div class="desc">Iced Long Black 4.9, Iced Latte or Iced Chocolate 5.9, Iced Mocha 6.2</div>
    <div class="sub">Soft Drinks 500ml 4 Jug 8</div><div class="desc">Cola, Diet Cola, Lemon Fizz, Lemonade, Soda Water, Raspberry Lemonade, Lemon Lime &amp; Bitters, Lime &amp; Soda, Soda Lime &amp; Bitters</div>
    <div class="sub">Mineral Water</div><div class="desc">Clearbrook Sparkling (Lighty/ Lemon/ Lime/ Rasberry) 450ml 4<br>Clearbrook Still 600ml 3, Palmwater Coconut water 330ml 4</div>
    <div class="sub">Fresh Squeezed Juices</div><div class="desc">Orange Juice 250ml 4 500ml 8</div>
    <div class="sub">Smoothies</div><div class="desc">ACAI 9 Choice of:<span class="gap">(1) Brazilian Super Acai pure OR energy, Banana and Almond Milk OR Apple Juice</span><span class="gap">(2) Cocoberry Bang Coconut Pack, Banana, Frozen mixed berries and Coconut water</span><span class="gap">LEAN &amp; GREEN Kale/Spinach, Cucumber, Celery &amp; Banana 9</span><span class="gap">MANGO Mango, Yogurt, Milk &amp; Honey 8</span><span class="gap">BANANA Banana, Yogurt, Milk, Honey &amp; Cinnamon 8</span><span class="gap">MIXED BERRY Mixed Berries, Yogurt, Milk &amp; Honey 8</span><span class="gap">ADD Protein Powder/ Chia Seed/ Oats 2</span><span class="gap">MILKSHAKES 8 Chocolate, Strawberry, Caramel</span><span class="gap">THICKSHAKES 10</span></div>
    <div class="sub">Beer &amp; Cider</div><div class="desc">BOTTLED BEER Goldfield Gold 5, Harbour Mid 5, Ridgeline Lager 6, Goldfield Summer 6, Harbour Draught 6, Regal Lager 6.5, Copperton Pale ale 6, Harbour Dry 6, Pale Crest 6, Yarrow Pale ale 6, Yarrow Golden 6, Bradley 6, Tollway New 6, Halden super dry 6, Crestline light 5, Tollway Old 6, Halden Light 5, Fairhaven 6, Tollway Extra Dry 6, Coastal 6</div>
    <div class="sub">Premix</div><div class="desc">Jed Barrel &amp; Cola 7.50 Northern Club Cola 7.5<br>Jock Dunmore &amp; Cola 8.00 Northern Club Dry 7.5, Pesca 7.5</div>
    <div class="sub">Bottled Cider</div><div class="desc">Summerfield Apple 7.5 Rosendal Passionfruit 7.5<br>Summerfield Pear 7.5 Rosendal Strawberry &amp; Lime 7.5</div>
    <div class="sub">Wine &amp; Champagne</div><div class="desc">RED WINE (house collection) Glass 150ml Glass 250ml Bottle (750ml)<br>Shiraz 7, 9, 29, Merlot 7, 9, 29, Cabernet Sauvignon 7, 9, 29<br>SPECIAL Shiraz (small bottle 187 ml) 8<span class="gap">WHITE WINE (house collection) Glass 150ml Glass 250ml Bottle (750ml)</span>Moscato 7, 9, 29, Sauvignon Blanc 7, 9, 29<br>SPECIAL Sauvignon Blanc (small bottle 187 ml) 8<span class="gap">ROSE WINE Glass 150ml Glass 250ml Bottle (750ml) Merlot Rose 7, 9, 29</span></div>
  </div>
</section>

<!-- Cover -->
<section class="panel panel--green arch" style="left:570px;top:606px;width:284px;height:594px">
  <svg class="deco" width="284" height="594"><circle cx="142" cy="336" r="122" fill="none" stroke="#fff" stroke-opacity=".7"/><circle cx="250" cy="480" r="8" fill="none" stroke="#fff"/></svg>
  <div class="brand" style="top:152px;font-size:38px;letter-spacing:4px">Verdella</div>
  <div class="brand" style="top:274px;font-size:54px;line-height:1;letter-spacing:2px">BISTRO<br>MENU</div>
  <div class="note" style="top:530px;font-size:13px">NO BYO</div>
  <div class="note" style="top:548px;font-size:8px">10% surcharge on public holidays</div>
</section>

</body>
</html>
```